website for LanternPeak Advisory - a HR Consultancy Company

Creation of a website template. I would like to make it with with Wix, but am open to other online website programms.

Website is for consulting company in human resources offering the following services:
- Human resources and talent management for small companies
- Human resources consulting for start-ups
- Diversity and Inclusion management/training
- Board of Directors - talent identification and need evalutation
- coaching and counseling

Pages needed:
- Home page
- HR and talent management
- HR consulting for start-ups
- Diversity & Inclusion management/training
- coaching and counseling
- contact

1. My logo below
2. an example website that I like (not in terms of colours): https://www.mapleridgeadvisors.ch/
http://www.veldorquint.ch/

Target Market(s)

small and mid-sized companies, start-ups

Industry/Entity Type

Consulting

Number of Pages Required

5+ page

Font styles to use
Serif
Sans Serif

Colors
3277b5
35a7d7

Requirements
Must have
• - easy on the eye yet professional looking
• - my text is short
• - website should be clear and easy to understand
Nice to have
• - I will include photographs of the coaches
Should not have
• too many colours
• complicated

```html
<!DOCTYPE html>
<html lang="en">
<head>
<meta charset="utf-8">
<title>LanternPeak Advisory – HR Consultancy</title>
<link href="https://fonts.googleapis.com/css2?family=Fira+Sans+Extra+Condensed:wght@400;600;700&family=Montserrat:wght@400;500;600;700&family=Roboto:wght@400;500&display=swap" rel="stylesheet">
<style>
:root{
  --brand:#3277b5;
  --brand-dark:#2c6aa5;
  --accent:#35a7d7;
  --ink:#1c1c1c;
  --muted:#6d6d6d;
  --white:#ffffff;
  --light:#eeeeee;
  --field:rgba(255,255,255,.35);
}
*{box-sizing:border-box;margin:0;padding:0}
html,body{width:1200px;height:2568px;overflow:hidden}
body{position:relative;background:var(--white);font-family:"Montserrat",sans-serif;color:var(--ink)}
.abs{position:absolute}

/* header */
.site-header{position:absolute;left:0;top:0;width:1200px;height:134px;background:var(--white)}
.social-square{left:56px;top:55px;width:24px;height:24px;background:var(--brand);border-radius:3px}
.menu-toggle{left:104px;top:55px;display:flex;align-items:center;gap:16px;font-size:19px;font-weight:500;letter-spacing:.5px;color:var(--ink)}
.menu-toggle .bars{width:33px;height:24px;display:flex;flex-direction:column;justify-content:space-between}
.menu-toggle .bars span{display:block;height:4px;background:var(--brand);border-radius:1px}
.brand-name{left:0;width:1200px;top:48px;text-align:center;font-family:"Montserrat",sans-serif;font-weight:700;font-size:30px;color:var(--brand);letter-spacing:.5px}
.contact-line{right:55px;display:flex;align-items:center;gap:16px;font-size:18px;color:var(--ink)}
.contact-line svg{width:24px;height:24px}
.contact-phone{top:38px}
.contact-mail{top:70px}

/* hero */
.hero{position:absolute;left:0;top:134px;width:1200px;height:609px;background:linear-gradient(180deg,#8e9194 0%,#6e6c68 35%,#6a5a45 65%,#4a4036 100%);overflow:hidden}
.hero-rule{left:510px;top:183px;width:180px;height:2px;background:rgba(255,255,255,.8)}
.hero-title{left:0;width:1200px;top:206px;text-align:center;font-family:"Fira Sans Extra Condensed",sans-serif;font-weight:700;font-size:84px;letter-spacing:1px;color:var(--white)}
.hero-sub{left:0;width:1200px;top:308px;text-align:center;font-family:"Fira Sans Extra Condensed",sans-serif;font-weight:400;font-size:48px;letter-spacing:2px;color:var(--white)}
.hero-cta{left:466px;top:400px;width:268px;height:41px;background:var(--white);border-radius:7px;display:flex;align-items:center;justify-content:center;font-family:"Fira Sans Extra Condensed",sans-serif;font-size:19px;letter-spacing:1px;color:var(--brand)}
.slider-dots{right:22px;top:563px;display:flex;gap:9px}
.slider-dots span{width:19px;height:19px;border-radius:50%;background:rgba(255,255,255,.45)}
.slider-dots span.active{background:var(--white)}

/* services */
.services{position:absolute;left:0;top:743px;width:1200px;height:385px;background:linear-gradient(135deg,#3a7fbd 0%,var(--brand) 50%,#2d6faa 100%)}
.section-rule{top:87px;height:2px;background:rgba(255,255,255,.7)}
.services-title{left:0;width:1200px;top:70px;text-align:center;font-size:23px;font-weight:500;letter-spacing:1.5px;color:var(--white)}
.service{top:130px;width:230px;text-align:center;color:var(--white)}
.service svg{width:80px;height:80px;display:block;margin:0 auto}
.service-name{margin-top:16px;font-family:"Roboto",sans-serif;font-size:16px;line-height:20px;height:40px}
.service-btn{display:block;margin:12px auto 0;width:130px;height:28px;line-height:28px;background:var(--white);border-radius:4px;font-family:"Fira Sans Extra Condensed",sans-serif;font-weight:600;font-size:14px;letter-spacing:1.5px;color:var(--brand)}

/* intro */
.intro-heading{left:0;width:1200px;top:1201px;text-align:center;font-family:"Roboto",sans-serif;font-size:22px;line-height:29px;color:var(--brand)}
.intro-col{top:1321px;width:370px;font-family:"Roboto",sans-serif;font-size:13px;line-height:17px;color:var(--ink)}
.intro-col p{margin-bottom:14px}
.intro-col b{font-weight:500}

/* team */
.team{position:absolute;left:0;top:1548px;width:1200px;height:400px;background:var(--light)}
.team-title{left:0;width:1200px;top:72px;text-align:center;font-size:23px;font-weight:500;letter-spacing:1px;color:var(--ink)}
.member{top:128px;width:191px;height:192px;background:linear-gradient(180deg,#f4f4f4 0%,#d9d9dc 100%)}
.member.highlight{background:var(--accent);color:var(--white);display:flex;flex-direction:column;align-items:center;justify-content:center;text-align:center}
.member-name{font-size:18px;font-weight:700;letter-spacing:.5px}
.member-role{font-family:"Roboto",sans-serif;font-size:16px;line-height:20px;margin-top:4px}

/* footer */
.site-footer{position:absolute;left:0;top:1948px;width:1200px;height:620px;background:linear-gradient(160deg,var(--brand) 0%,#3076b4 55%,#2a68a2 100%);color:var(--white)}
.footer-brand{left:0;width:1200px;top:80px;text-align:center;font-weight:700;font-size:30px;letter-spacing:.5px;color:var(--white)}
.footer-rule{left:140px;width:918px;height:1px;background:rgba(255,255,255,.5)}
.footer-col{top:226px}
.footer-col h3{font-size:16px;font-weight:600;margin-bottom:8px}
.footer-col li{list-style:none;font-size:13px;line-height:24px}
.field{left:692px;width:366px;background:var(--field);border-radius:4px;font-size:13px;padding:6px 12px}
.submit-btn{left:692px;top:403px;width:99px;height:28px;background:var(--white);border-radius:4px;text-align:center;line-height:28px;font-family:"Fira Sans Extra Condensed",sans-serif;font-weight:600;font-size:14px;letter-spacing:1.5px;color:var(--brand)}
.copyright{left:140px;top:502px;font-size:14px;font-weight:600}
</style>
</head>
<body>

<header class="site-header">
  <a class="abs social-square" aria-label="Social profile"></a>
  <div class="abs menu-toggle"><span class="bars"><span></span><span></span><span></span></span>MENU</div>
  <div class="abs brand-name">LanternPeak Advisory</div>
  <div class="abs contact-line contact-phone">(000) 000-0000
    <svg viewBox="0 0 24 24"><rect width="24" height="24" rx="3" fill="#3277b5"/><path d="M8 5l2.5 3-1.5 1.5c.8 2 2.5 3.7 4.5 4.5L15 12.5l3 2.5-1.5 3C11 17.5 6.5 13 6 6.5z" fill="#fff"/></svg>
  </div>
  <div class="abs contact-line contact-mail">example@lanternpeak.com
    <svg viewBox="0 0 24 24"><rect width="24" height="24" rx="3" fill="#35a7d7"/><rect x="5" y="7" width="14" height="10" fill="none" stroke="#fff" stroke-width="1.6"/><path d="M5 7l7 6 7-6" fill="none" stroke="#fff" stroke-width="1.6"/></svg>
  </div>
</header>

<section class="hero" role="img" aria-label="Blurred photograph of a mountain ridge under a cloudy sky">
  <div class="abs hero-rule"></div>
  <h1 class="abs hero-title">LANTERNPEAK ADVISORY</h1>
  <p class="abs hero-sub">A HR CONSULTANCY COMPANY</p>
  <a class="abs hero-cta">GET IN CONTACT WITH US TODAY</a>
  <div class="abs slider-dots"><span></span><span class="active"></span><span></span></div>
</section>

<section class="services">
  <div class="abs section-rule" style="left:140px;width:283px"></div>
  <div class="abs section-rule" style="left:777px;width:281px"></div>
  <h2 class="abs services-title">SOME OF OUR SERVICES</h2>

  <div class="abs service" style="left:132px">
    <svg viewBox="0 0 80 80"><circle cx="40" cy="40" r="35" fill="none" stroke="#fff" stroke-width="5"/><circle cx="40" cy="32" r="12" fill="#fff"/><path d="M18 64c4-12 12-16 22-16s18 4 22 16a35 35 0 0 1-44 0z" fill="#fff"/></svg>
    <div class="service-name">HR Consulting<br>for Start-ups</div>
    <a class="service-btn">VIEW SERVICE</a>
  </div>
  <div class="abs service" style="left:368px">
    <svg viewBox="0 0 80 80"><path d="M4 32L40 18l36 14-36 14z" fill="#fff"/><path d="M20 40v16c0 6 40 6 40 0V40L40 48z" fill="#fff"/><path d="M70 34v18" stroke="#fff" stroke-width="3"/><circle cx="70" cy="54" r="3" fill="#fff"/></svg>
    <div class="service-name">Board of Directors -<br>Talent Identification</div>
    <a class="service-btn">VIEW SERVICE</a>
  </div>
  <div class="abs service" style="left:602px">
    <svg viewBox="0 0 80 80"><rect x="34" y="2" width="12" height="8" fill="#fff"/><circle cx="40" cy="45" r="32" fill="#fff"/><path d="M40 45V22a23 23 0 0 1 23 23z" fill="#3277b5"/></svg>
    <div class="service-name">Diversity and Inclusion<br>Training</div>
    <a class="service-btn">VIEW SERVICE</a>
  </div>
  <div class="abs service" style="left:837px">
    <svg viewBox="0 0 80 80"><circle cx="20" cy="28" r="8" fill="#fff"/><circle cx="60" cy="28" r="8" fill="#fff"/><path d="M4 60c0-14 6-20 16-20s16 6 16 20zM44 60c0-14 6-20 16-20s16 6 16 20z" fill="#fff"/><circle cx="40" cy="24" r="11" fill="#fff" stroke="#3277b5" stroke-width="2"/><path d="M18 66c0-18 9-26 22-26s22 8 22 26z" fill="#fff" stroke="#3277b5" stroke-width="2"/></svg>
    <div class="service-name">HR &amp; Talent Management<br>for Small Companies</div>
    <a class="service-btn">VIEW SERVICE</a>
  </div>
</section>

<h2 class="abs intro-heading">We’re LanternPeak Advisory,<br>an established and developed Human<br>Resources Consultancy team</h2>
<div class="abs intro-col" style="left:219px">
  <p>Here is a small section of text with a brief introduction of the company. <b>See our services</b> dolor sit amet, consectetur adipiscing elit, sed do eiusmod tempor incididunt <b>get in touch</b> et dolore magna aliqua.</p>
  <p>Lorem ipsum dolor sit amet, consectetur adipiscing elit, sed do eiusmod tempor <b>meet the team</b> incididunt ut labore et dolore magna aliqua.</p>
</div>
<div class="abs intro-col" style="left:611px">
  <p>Lorem ipsum dolor sit amet, consectetur adipiscing elit, sed do eiusmod tempor <b>learn more about us</b> incididunt ut labore et dolore magna aliqua.</p>
  <p><b>HR Consultancy Training</b> dolor sit amet, consectetur adipiscing elit, sed do eiusmod tempor incididunt et dolore magna aliqua. Lorem ipsum dolor <b>Consulting for Start-ups</b> sit amet, consectetur adipiscing elit, sed do incididunt ut labore et dolore magna aliqua.</p>
</div>

<section class="team">
  <h2 class="abs team-title">PART OF THE TEAM</h2>
  <div class="abs member" style="left:151px" role="img" aria-label="Portrait of a team member in a dark suit"></div>
  <div class="abs member highlight" style="left:385px" role="img" aria-label="Portrait of Nora Whitfield, HR Consultancy Trainer">
    <div class="member-name">NORA WHITFIELD</div>
    <div class="member-role">HR Consultancy<br>Trainer</div>
  </div>
  <div class="abs member" style="left:621px" role="img" aria-label="Portrait of a team member in a dark blazer"></div>
  <div class="abs member" style="left:856px" role="img" aria-label="Portrait of a team member in a dark suit"></div>
</section>

<footer class="site-footer">
  <div class="abs footer-brand">LanternPeak Advisory</div>
  <div class="abs footer-rule" style="top:189px"></div>
  <div class="abs footer-col" style="left:140px">
    <h3>Site Links</h3>
    <ul><li>Home</li><li>About us</li><li>Get in touch</li><li>Our services</li><li>Privacy policy</li><li>Terms and conditions</li><li>Site map</li></ul>
  </div>
  <div class="abs footer-col" style="left:377px">
    <h3>Our Services</h3>
    <ul><li>Talent Management for Small Companies</li><li>Consulting for Start-ups</li><li>Diversity and Inclusion Training</li><li>Board of Directors - Talent Identification</li><li>Coaching and Counseling</li></ul>
  </div>
  <div class="abs footer-col" style="left:692px"><h3>Quick Contact</h3></div>
  <div class="abs field" style="top:255px;height:28px">Name</div>
  <div class="abs field" style="top:296px;height:28px">Email</div>
  <div class="abs field" style="top:337px;height:51px">Message</div>
  <a class="abs submit-btn">SUBMIT</a>
  <div class="abs footer-rule" style="top:486px"></div>
  <p class="abs copyright">© LanternPeak Advisory 2017. All Rights Reserved</p>
</footer>

</body>
</html>
```